Rocket business card

Modern business card design, use of color is good with clean space too.

Things to include on card:

Quote: I add fuel to your optometry practice

- Eyewear Sales
- Admin Duties
- Revenue Collection
- Leadership
- Tech Adoption
- COGS Reduction
- Product Sourcing
-Medical Growth

Dalton Vessey, CEO
Glint Harbor
Text Me! 847-302-1964
dalton@glintharbor.example

```html
<!DOCTYPE html>
<html lang="en">
<head>
<meta charset="utf-8">
<title>Glint Harbor — Business Card</title>
<link href="https://fonts.googleapis.com/css2?family=Open+Sans:wght@400;600;700;800&display=swap" rel="stylesheet">
<style>
  :root {
    --bg: #3a3532;
    --card: #0b0b0c;
    --white: #ffffff;
    --red: #e2382a;
    --orange: #f08a1c;
    --amber: #f5a623;
  }
  * { margin: 0; padding: 0; box-sizing: border-box; }
  html, body { width: 1200px; height: 716px; overflow: hidden; }
  body {
    background: var(--bg);
    font-family: "Open Sans", Arial, sans-serif;
    color: var(--white);
    display: flex;
    align-items: center;
    justify-content: center;
    gap: 40px;
  }
  .card {
    width: 540px;
    height: 309px;
    background: var(--card);
    border-radius: 3px;
    box-shadow: 0 18px 40px rgba(0,0,0,.45);
    position: relative;
    overflow: hidden;
  }
  .brand {
    display: flex;
    align-items: center;
    gap: 12px;
  }
  .brand-dot {
    width: 38px; height: 38px;
    border-radius: 50%;
    background: var(--orange);
    flex: none;
  }
  .brand-name {
    font-weight: 600;
    font-size: 26px;
    letter-spacing: 2px;
    color: var(--white);
    text-transform: uppercase;
    white-space: nowrap;
  }

  /* Services side */
  .card--services .brand {
    position: absolute;
    top: 70px; left: 0; right: 0;
    justify-content: center;
  }
  .services-rule {
    position: absolute;
    top: 150px; left: 30px; right: 30px;
    display: flex; align-items: center; gap: 14px;
  }
  .services-rule::before, .services-rule::after {
    content: ""; flex: 1; height: 1px;
    background: linear-gradient(90deg, var(--amber), var(--red));
  }
  .services-rule::after { background: linear-gradient(90deg, var(--red), var(--amber)); }
  .services-title { font-weight: 700; font-size: 15px; font-style: italic; }
  .services-list {
    position: absolute;
    top: 178px; left: 20px; right: 20px;
    list-style: none;
    display: flex; flex-wrap: wrap; justify-content: center;
    column-gap: 16px; row-gap: 10px;
    font-size: 12.5px;
  }
  .services-list li { display: flex; align-items: center; gap: 5px; }
  .services-list li::before {
    content: ""; width: 5px; height: 5px; border-radius: 50%;
    background: var(--orange);
  }
  .services-list .row-break { flex-basis: 100%; height: 0; }
  .services-list .row-break::before { display: none; }

  /* Contact side */
  .card--contact .brand {
    position: absolute;
    top: 130px; left: 34px;
  }
  .brand--contact .brand-name { font-size: 22px; }
  .contact-divider {
    position: absolute;
    left: 268px; top: 92px;
    width: 1px; height: 130px;
    background: linear-gradient(180deg, var(--amber), var(--red));
  }
  .contact {
    position: absolute;
    left: 292px; top: 104px;
  }
  .contact-name {
    font-weight: 800;
    font-size: 22px;
    letter-spacing: 1px;
    text-transform: uppercase;
    background: linear-gradient(90deg, var(--red), var(--amber));
    -webkit-background-clip: text;
    background-clip: text;
    color: transparent;
    white-space: nowrap;
  }
  .contact-role { font-size: 13px; margin-top: 1px; }
  .contact-lines { margin-top: 22px; font-size: 13px; line-height: 1.55; }
</style>
</head>
<body>
  <section class="card card--services" aria-label="Card back: services">
    <div class="brand">
      <span class="brand-dot"></span>
      <span class="brand-name">Glint Harbor</span>
    </div>
    <div class="services-rule"><span class="services-title">Our Services</span></div>
    <ul class="services-list">
      <li>Eyewear Sales</li>
      <li>Admin Duties</li>
      <li>Revenue Collection</li>
      <li>Leadership</li>
      <li class="row-break" aria-hidden="true"></li>
      <li>Tech Adoption</li>
      <li>COGS Reduction</li>
      <li>Product Sourcing</li>
      <li>Medical Growth</li>
    </ul>
  </section>

  <section class="card card--contact" aria-label="Card front: contact">
    <div class="brand brand--contact">
      <span class="brand-dot"></span>
      <span class="brand-name">Glint Harbor</span>
    </div>
    <div class="contact-divider"></div>
    <div class="contact">
      <h1 class="contact-name">Dalton Vessey</h1>
      <p class="contact-role">CEO</p>
      <div class="contact-lines">
        <p>Text Me! 847-302-1964</p>
        <p>dalton@glintharbor.example</p>
      </div>
    </div>
  </section>
</body>
</html>
```